Label for new gin: Kliff7 - Distilled Gin

Artistic label with local elements for new gin brand.
Dunes, lighthouses, sea, seagulls, ships.
Fresh lemon gin with fine juniper notes. Manufactured directly on the Baltic Sea in Warnemünde. Should be scalable. 4x6inch or larger.
Motifs put together artistically. Photos of the place in the attachment. The name of the gin comes from the beach entrance 3 (hence dune 3). A dune stalk (blue oat) is in the bottle. Bottle will be a clear glass apothecary bottle 500ml.
Updates

Niedrige Design-Qualität

Target Market(s)

spirits

Industry/Entity Type

Getränke

Font styles to use
Decorative
Script

Colors

Designer to choose colors to be used in the design.

Requirements
Must have
• Sketch, Handdrawn Style /// 500ml, 41% vol Alc "Made by QMTO GmbH Farnstieg 22a Roggentin" "Bottled in Warnemünde" "Kliff7" "Distilled Gin" "Inspired by the sea"

```html
<!DOCTYPE html>
<html lang="en">
<head>
<meta charset="utf-8">
<title>Kliff7 Distilled Gin – Label</title>
<link rel="stylesheet" href="https://fonts.googleapis.com/css2?family=Playfair+Display:ital,wght@0,700;1,400&family=Great+Vibes&family=Raleway:wght@300;400&display=swap">
<style>
  :root {
    --paper: #ffffff;
    --ink: #1c1a1a;
    --gold: #b5a46c;
    --sky: #cfe0ee;
    --sand: #ece4c8;
  }
  * { margin: 0; padding: 0; box-sizing: border-box; }
  html, body {
    width: 1200px;
    height: 1029px;
    overflow: hidden;
    background: var(--paper);
  }
  .label {
    position: relative;
    width: 1200px;
    height: 1029px;
    background: var(--paper);
    color: var(--ink);
  }
  .brand-name,
  .brand-number,
  .product-type,
  .tagline,
  .maker {
    position: absolute;
    left: 0;
    right: 0;
    text-align: center;
    line-height: 1;
    white-space: nowrap;
  }
  .brand-name {
    top: 432px;
    padding-left: 6px;
    font-family: "Playfair Display", serif;
    font-weight: 700;
    font-size: 62px;
    letter-spacing: -1px;
  }
  .brand-number {
    top: 475px;
    padding-left: 6px;
    font-family: "Playfair Display", serif;
    font-weight: 700;
    font-size: 75px;
    font-variant-numeric: lining-nums;
  }
  .product-type {
    top: 566px;
    padding-left: 6px;
    font-family: "Playfair Display", serif;
    font-style: italic;
    font-weight: 400;
    font-size: 21px;
    letter-spacing: 3px;
    color: var(--gold);
  }
  .tagline {
    top: 589px;
    padding-left: 6px;
    font-family: "Great Vibes", cursive;
    font-size: 26px;
  }
  .scene-art {
    position: absolute;
    left: 497px;
    top: 636px;
    width: 224px;
    height: 93px;
  }
  .maker {
    top: 733px;
    padding-left: 14px;
    font-family: "Raleway", sans-serif;
    font-weight: 400;
    font-size: 10px;
    line-height: 12.5px;
    color: var(--gold);
  }
  .volume,
  .strength {
    position: absolute;
    top: 763px;
    font-family: "Raleway", sans-serif;
    font-weight: 400;
    font-size: 16.5px;
    line-height: 1;
    white-space: nowrap;
  }
  .volume { left: 510px; }
  .strength { left: 626px; }
</style>
</head>
<body>
  <main class="label">
    <h1 class="brand-name">KLIFF</h1>
    <div class="brand-number">7</div>
    <p class="product-type">DISTILLED GIN</p>
    <p class="tagline">Inspired by the sea</p>

    <svg class="scene-art" viewBox="0 0 224 93" role="img" aria-label="Sketched coastal scene: lighthouse and curved-roof pavilion behind dune grass under a pale blue sky">
      <defs>
        <linearGradient id="coastTone" x1="0" y1="0" x2="0" y2="1">
          <stop offset="0" stop-color="var(--sky)"/>
          <stop offset="0.6" stop-color="#e4ebf0"/>
          <stop offset="1" stop-color="var(--sand)"/>
        </linearGradient>
      </defs>
      <rect x="0" y="0" width="224" height="93" fill="url(#coastTone)" opacity="0.8"/>
    </svg>

    <p class="maker">Made by QMTO GmbH Farnstieg 22a Roggentin<br>Bottled in Warnemünde</p>
    <p class="volume">500ml</p>
    <p class="strength">alc. 41% vol</p>
  </main>
</body>
</html>
```